Celestine Varga Gymnastics Center Business Card

Develop a business card with my CV logo provided. A classy and unique design using the colors black, white, purple and maybe a splash of gold. Add Address (918 S. Harlan Lane Medina, Ohio 44871), email (CelestineVargaGymnasticsCtr@mailbrook.com, website (www.CelestineVargaGymnasticsCenter.com), phone number (330-555-0192) on the card. Social media if there's room also. t: @VargaGym, i: @VargaGym, f: @CelestineVargaGymnasticsCenter

Target Market(s)

Families, children, gymnastics community and beyond

Industry/Entity Type

Business

Contact Information for Business Card

Add name (Celestine Varga) who is the owner. Add logo, add address details, classy font, uniqueness important, rounded edges on business card. Horizontal business card needed.

Font styles to use
Serif
Sans Serif

Colors
6b449b
ffffff

Requirements
Must have
• Must have logo, owner name and owner on card, must have colors purple, white, black where needed in print, and a splash of gold if appropriate. Keep card classy and clean. Must have address of location, phone number, website of business, email and social media.
Nice to have
• I am open here, but I'd appreciate uniqueness. Must be a lasting image for branding...
Should not have
• No kid-like looks...

```html
<!DOCTYPE html>
<html lang="en">
<head>
<meta charset="utf-8">
<title>Celestine Varga Gymnastics Center – Business Card</title>
<link rel="stylesheet" href="https://fonts.googleapis.com/css2?family=Lato:wght@400;700;900&display=swap">
<style>
  :root {
    --purple: #6b449b;
    --black: #111111;
    --ink: #1a1a1a;
    --white: #ffffff;
    --silver: #d4d4d4;
    --stage: #2b2b2b;
  }
  * { box-sizing: border-box; margin: 0; padding: 0; }
  html, body { width: 1200px; height: 880px; overflow: hidden; }
  body {
    background: var(--stage);
    position: relative;
    font-family: "Lato", sans-serif;
  }
  .card {
    position: absolute;
    width: 620px;
    height: 354px;
    border-radius: 22px;
    overflow: hidden;
  }
  /* Back */
  .card-back {
    left: 70px; top: 70px;
    background: var(--black);
  }
  .back-brand {
    position: absolute;
    left: 0; right: 0; top: 118px;
    display: flex;
    justify-content: center;
    align-items: center;
    gap: 14px;
  }
  .back-dot {
    width: 22px; height: 22px; border-radius: 50%;
    background: var(--silver);
    flex: none;
  }
  .back-name {
    font-weight: 700;
    font-size: 30px;
    line-height: 1.1;
    color: var(--silver);
    text-transform: uppercase;
    letter-spacing: 1px;
  }
  .back-url {
    position: absolute;
    left: 0; right: 0; bottom: 58px;
    text-align: center;
    color: var(--white);
    font-size: 15px;
    letter-spacing: 0.3px;
  }
  /* Front */
  .card-front {
    left: 510px; top: 456px;
    background: var(--white);
  }
  .edge-dot {
    position: absolute;
    left: -17px; top: 112px;
    width: 34px; height: 34px;
    border-radius: 50%;
    background: var(--purple);
  }
  .owner {
    position: absolute;
    left: 34px; top: 104px;
  }
  .owner-name {
    font-weight: 900;
    font-size: 20px;
    color: var(--ink);
    line-height: 1.05;
  }
  .owner-title {
    font-size: 16px;
    color: var(--purple);
    line-height: 1.05;
  }
  .brand {
    position: absolute;
    right: 36px; top: 40px;
    display: flex;
    align-items: center;
    gap: 10px;
  }
  .brand-dot {
    width: 18px; height: 18px;
    background: var(--purple);
    border-radius: 50%;
    flex: none;
  }
  .brand-name {
    font-weight: 900;
    font-size: 19px;
    line-height: 1.1;
    color: var(--ink);
    text-transform: uppercase;
  }
  .contacts {
    position: absolute;
    left: 34px; bottom: 26px;
    list-style: none;
  }
  .contacts li {
    display: flex;
    align-items: center;
    gap: 7px;
    font-size: 14.5px;
    color: var(--ink);
    line-height: 1.45;
  }
  .icon { width: 15px; height: 15px; flex: none; }
  .contacts li.socials {
    margin-top: 8px;
    gap: 9px;
  }
  .social { display: flex; align-items: center; gap: 6px; }
  .social-dot {
    width: 13px; height: 13px; border-radius: 50%;
    background: var(--purple);
  }
  .divider { width: 1px; height: 16px; background: var(--purple); }
</style>
</head>
<body>

<section class="card card-back">
  <div class="back-brand">
    <span class="back-dot"></span>
    <span class="back-name">Celestine Varga<br>Gymnastics Center</span>
  </div>
  <p class="back-url">www.CelestineVargaGymnasticsCenter.com</p>
</section>

<section class="card card-front">
  <span class="edge-dot"></span>

  <div class="brand">
    <span class="brand-dot"></span>
    <span class="brand-name">Celestine Varga<br>Gymnastics Center</span>
  </div>

  <div class="owner">
    <p class="owner-name">Celestine Varga</p>
    <p class="owner-title">Owner</p>
  </div>

  <ul class="contacts">
    <li>
      <svg class="icon" viewBox="0 0 16 16"><circle cx="8" cy="8" r="8" fill="var(--purple)"/><path d="M8 3.4a3 3 0 0 0-3 3c0 2.2 3 6.2 3 6.2s3-4 3-6.2a3 3 0 0 0-3-3z" fill="#fff"/><circle cx="8" cy="6.4" r="1.1" fill="var(--purple)"/></svg>
      918 S. Harlan Lane, Medina, Ohio 44871
    </li>
    <li>
      <svg class="icon" viewBox="0 0 16 16"><circle cx="8" cy="8" r="8" fill="var(--purple)"/><path d="M5.2 4.2l1.4 1.8-.8 1c.5 1.1 1.3 1.9 2.3 2.4l1-.8 1.8 1.4-.7 1.2c-2.8-.3-5.5-3-5.8-5.8z" fill="#fff"/></svg>
      (330-555-0192)
    </li>
    <li>
      <svg class="icon" viewBox="0 0 16 16"><circle cx="8" cy="8" r="8" fill="var(--purple)"/><rect x="4" y="5.2" width="8" height="5.6" fill="#fff"/><path d="M4 5.4l4 3 4-3" fill="none" stroke="var(--purple)" stroke-width="0.9"/></svg>
      CelestineVargaGymnasticsCtr@mailbrook.com
    </li>
    <li>
      <svg class="icon" viewBox="0 0 16 16"><circle cx="8" cy="8" r="8" fill="var(--purple)"/><g fill="none" stroke="#fff" stroke-width="0.9"><circle cx="8" cy="8" r="4.2"/><ellipse cx="8" cy="8" rx="1.8" ry="4.2"/><path d="M3.8 8h8.4"/></g></svg>
      www.CelestineVargaGymnasticsCenter.com
    </li>
    <li class="socials">
      <span class="social"><span class="social-dot"></span>@VargaGym</span>
      <span class="divider"></span>
      <span class="social"><span class="social-dot"></span>@VargaGym</span>
      <span class="divider"></span>
      <span class="social"><span class="social-dot"></span>@CelestineVargaGymnasticsCenter</span>
    </li>
  </ul>
</section>

</body>
</html>
```